Safety Consultancy focusing on developing exceptional Safety Leaders

I need a full but simple, modern, catchy website to drive business - my focus is on helping organizations to understand the impact that leaders have on safety performance and how they build the processes to make that happen. I already have great branding (logos) built through PixelGuild and can provide all narrative to build out the pages

Target Market(s)

Focused internationally. Typical client has a fairly robust and mature safety culture yet lacks the focused effort to develop all levels of leadership in terms of managing safety. Exercising these competencies results in continued development of an organizations safety culture as well as improved safety performance

Industry/Entity Type

all

Coding

Coded - Design and coding required

Number of Pages Required

4 page

Font styles to use
Other font styles liked:
• to match my branding

Colors
0054AA
0677BA
7BADD7
CADEEF
E8F1F8

Requirements
Must have
• Must utilize my current branding, logo, etc. I want to have a page outlining clearly my vision - which I will add to my uploads as we move forward. I need to have a page listing my extensive and unique experience as well as successes
Nice to have
• Want to leave it up to designers - but needs to be simple and easily navigable - hope to have a resource page that I can update myself with safety resource info, reports, etc.

```html
<!DOCTYPE html>
<html lang="en">
<head>
<meta charset="utf-8">
<title>Corvane — Safety Leadership Consultancy</title>
<link rel="stylesheet" href="https://fonts.googleapis.com/css2?family=Fira+Sans:wght@400;500;600;700&family=Open+Sans:wght@400;600;700&family=Tinos&display=swap">
<style>
:root{
  --navy:#0d2260;
  --navy-deep:#0b1233;
  --blue:#0b7fe0;
  --blue-dark:#0054aa;
  --ink:#1d2b4f;
  --text:#6b7280;
  --grey-bg:#f1f1f1;
  --soft-bg:#f5f6f9;
  --white:#ffffff;
  --line:#d5d9e0;
}
*{box-sizing:border-box;margin:0;padding:0}
html,body{width:1200px;height:4298px;overflow:hidden}
body{position:relative;background:var(--white);font-family:"Open Sans",sans-serif;color:var(--ink)}
.abs{position:absolute}
h1,h2,h3,h4{font-family:"Fira Sans",sans-serif}
.accent{color:var(--blue)}
.eyebrow{font-size:12px;color:var(--blue-dark);letter-spacing:.3px;text-transform:uppercase;border-bottom:2px solid var(--blue);padding-bottom:4px;display:inline-block}

.site-header{left:0;top:0;width:1200px;height:145px;background:#f3f6fc}
.brand{display:flex;align-items:center;gap:12px}
.brand-dot{width:34px;height:34px;border-radius:50%;background:var(--blue)}
.brand-name{font-family:"Fira Sans",sans-serif;font-weight:600;font-size:36px;color:#3b2c84}
.contact-item{display:flex;gap:12px;align-items:center;font-family:Arial,sans-serif;font-size:13px;color:#333;line-height:20px}
.contact-item svg{flex:none}
.main-nav{left:244px;top:110px;width:878px;height:54px;background:var(--white);border-radius:27px;box-shadow:0 2px 6px rgba(0,0,0,.12);display:flex;align-items:center;padding-left:66px;font-family:Arial,sans-serif;font-size:14px;color:#333;z-index:3}
.main-nav a{color:#333;text-decoration:none;margin-right:30px}
.btn-appointment{position:absolute;right:0;top:2px;width:158px;height:46px;border-radius:23px;background:var(--blue);color:#fff;display:flex;align-items:center;justify-content:center;font-size:14px;box-shadow:0 2px 4px rgba(0,0,0,.3)}

.hero{left:0;top:145px;width:1200px;height:920px}
.hero-box{left:92px;width:532px;height:300px;background:rgba(40,55,95,.55)}
.hero-box .bar{position:absolute;left:0;top:42px;width:4px;height:88px;background:var(--blue)}
.hero-box h1{position:absolute;left:27px;top:32px;font-size:40px;line-height:50px;color:#fff;font-weight:600;letter-spacing:.5px}
.hero-box p{position:absolute;left:27px;top:140px;width:490px;font-size:14.5px;line-height:29px;color:#fff}
.btn-solid{background:var(--blue);color:#fff;font-weight:700;font-size:14px;display:flex;align-items:center;justify-content:center}

.about-text{left:604px;top:992px;width:460px}
.about-text h2{font-size:38px;line-height:46px;color:var(--navy);font-weight:600;margin-top:22px}
.about-text h3{font-size:19px;color:var(--navy);font-weight:500;margin-top:26px}
.about-text p{font-size:12px;line-height:19.5px;color:var(--text);margin-top:16px}
.btn-contact{margin-top:24px;width:136px;height:40px;gap:12px;font-size:14px}

.services{left:0;top:1432px;width:1200px;height:663px;background:var(--grey-bg)}
.center-head{width:1200px;text-align:center}
.center-head h2{font-size:42px;color:var(--navy);font-weight:600;margin-top:14px}
.service-card{width:305px;height:370px}
.service-photo{position:absolute;left:0;top:0;width:305px;height:280px}
.service-body{position:absolute;left:67px;top:229px;width:238px;height:138px;background:#fff;box-shadow:0 2px 6px rgba(0,0,0,.08);padding:30px 22px}
.service-body h4{font-size:16px;font-weight:600;color:var(--ink)}
.service-body p{font-size:12.5px;line-height:21px;color:var(--text);margin-top:12px}
.service-icon{position:absolute;left:38px;top:198px;width:60px;height:60px;border-radius:50%;background:var(--blue);display:flex;align-items:center;justify-content:center;border:3px solid #fff}

.why{left:0;top:2095px;width:1200px;height:575px;background:linear-gradient(90deg,#0b2a78 0%,#0c2567 60%,#0a1d55 100%)}
.why-text{left:621px;top:2143px;width:500px;color:#fff}
.why-text .eyebrow{color:var(--blue);font-size:11.5px}
.why-text h2{font-size:37px;line-height:46px;font-weight:600;margin-top:14px}
.why-item{left:624px;width:444px;height:105px;background:rgba(60,80,150,.45);border-left:4px solid #8aa0d0;display:flex;align-items:center;padding-left:28px;gap:30px;color:#fff}
.why-item h4{font-size:14px;font-weight:600;font-family:"Open Sans",sans-serif}
.why-item p{font-size:12.5px;line-height:20px;color:#d4dbee;margin-top:2px}

.testimonials{left:0;top:2670px;width:1200px;height:610px;background:var(--soft-bg)}
.quote-card{width:305px;height:174px;background:#fff;padding:28px 22px;font-size:15px;line-height:23px;color:#444;box-shadow:0 2px 6px rgba(0,0,0,.05)}
.quote-card.active{background:var(--blue);color:#fff}
.quote-tail{width:0;height:0;border-top:22px solid var(--blue);border-right:22px solid transparent}
.author{display:flex;align-items:center;gap:20px}
.avatar{width:54px;height:54px;border-radius:50%;background:linear-gradient(135deg,#9aa7b8,#4b5566);border:3px solid #fff}
.author strong{display:block;font-size:14px;color:var(--ink)}
.author span{font-size:12.5px;color:#999}

.contact-title{left:0;top:3330px;width:1200px;text-align:center;font-family:"Tinos",serif;font-size:46px;font-weight:400;color:#222}
.contact-box{left:147px;top:3430px;width:908px;height:292px;background:#fff;box-shadow:0 3px 12px rgba(0,0,0,.1)}
.address-panel{position:absolute;left:0;top:0;width:304px;height:292px;background:#eeeeee;padding:30px 33px}
.address-panel h3{font-family:"Tinos",serif;font-weight:400;font-size:36px;color:#222}
.addr-row{display:flex;gap:12px;font-size:14px;line-height:20px;color:#222;margin-top:18px}
.field{position:absolute;border-bottom:1px solid #999;font-size:13px;color:#333;height:30px}
.btn-enquiry{position:absolute;left:325px;top:217px;width:186px;height:37px;border-radius:19px;background:var(--blue);color:#fff;font-family:"Tinos",serif;font-size:14px;display:flex;align-items:center;justify-content:center;gap:10px;letter-spacing:.3px}

.footer-bg{left:0;top:3660px;width:1200px;height:638px}
.footer-block{color:#fff;display:flex;align-items:center;gap:12px;border-top:6px solid #26304d;border-bottom:6px solid #26304d;height:56px}
.footer-nav{left:0;top:4212px;width:1200px;display:flex;justify-content:center;font-size:12.5px;color:#fff}
.footer-nav a{color:#fff;text-decoration:none;margin:0 22px}
.social{display:flex;gap:8px;justify-content:center}
.social span{width:20px;height:20px;border-radius:50%;background:#fff}
</style>
</head>
<body>

<header class="abs site-header">
  <div class="abs brand" style="left:103px;top:42px">
    <span class="brand-dot"></span><span class="brand-name">Corvane</span>
  </div>
  <div class="abs contact-item" style="left:414px;top:34px">
    <svg width="40" height="40" viewBox="0 0 40 40"><rect x="8" y="8" width="24" height="24" transform="rotate(45 20 20)" fill="none" stroke="#3cc7a8" stroke-width="1.5"/><path d="M20 13a5 5 0 0 1 5 5c0 4-5 9-5 9s-5-5-5-9a5 5 0 0 1 5-5z" fill="#3cc7a8"/><circle cx="20" cy="18" r="1.8" fill="#fff"/></svg>
    <div>Email Address<br>mira@corvane-mail.com</div>
  </div>
  <div class="abs contact-item" style="left:659px;top:34px">
    <svg width="40" height="40" viewBox="0 0 40 40"><rect x="8" y="8" width="24" height="24" transform="rotate(45 20 20)" fill="none" stroke="#3cc7a8" stroke-width="1.5"/><path d="M20 13a5 5 0 0 1 5 5c0 4-5 9-5 9s-5-5-5-9a5 5 0 0 1 5-5z" fill="#3cc7a8"/><circle cx="20" cy="18" r="1.8" fill="#fff"/></svg>
    <div>Email Address<br>mira@corvane-mail.com</div>
  </div>
  <div class="abs contact-item" style="left:905px;top:34px">
    <svg width="40" height="40" viewBox="0 0 40 40"><rect x="8" y="8" width="24" height="24" transform="rotate(45 20 20)" fill="none" stroke="#3cc7a8" stroke-width="1.5"/><path d="M20 13a5 5 0 0 1 5 5c0 4-5 9-5 9s-5-5-5-9a5 5 0 0 1 5-5z" fill="#3cc7a8"/><circle cx="20" cy="18" r="1.8" fill="#fff"/></svg>
    <div>Email Address<br>mira@corvane-mail.com</div>
  </div>
</header>
<nav class="abs main-nav">
  <a>Home</a><a style="margin-left:30px">About Us</a><a>Services</a><a>Our Team</a><a style="margin-left:10px">Projects</a>
  <span class="btn-appointment">Appointment</span>
</nav>

<section class="abs hero">
  <svg width="1200" height="920" viewBox="0 0 1200 920" style="position:absolute;left:0;top:0">
    <defs>
      <linearGradient id="heroFill" x1="0" y1="0" x2="1" y2="0.4">
        <stop offset="0" stop-color="#0e2b6e"/><stop offset=".55" stop-color="#3f5a8c"/><stop offset="1" stop-color="#8b9db7"/>
      </linearGradient>
    </defs>
    <g role="img" aria-label="Photo of safety engineers with a laptop inspecting an industrial facility">
      <rect width="1200" height="920" fill="url(#heroFill)"/>
    </g>
    <path d="M0 685 C300 640 520 640 700 665 C900 695 1080 780 1200 900 L1200 920 L0 920 Z" fill="#fff"/>
    <path d="M476 665 C780 655 1040 730 1200 870 L1200 900 C1060 770 800 690 476 665 Z" fill="#0b7fe0"/>
  </svg>
  <div class="abs hero-box" style="top:200px">
    <span class="bar"></span>
    <h1>Navigating Safety with<br>Expertise</h1>
    <p>It is a long and established fact that a reader will be distracted by the readable content of a page when looking.</p>
    <div class="btn-solid" style="position:absolute;left:26px;top:222px;width:197px;height:45px">REQUEST A DEMO</div>
  </div>
</section>

<svg class="abs" style="left:0;top:1010px" width="490" height="425" viewBox="0 0 490 425">
  <path d="M0 25 C120 -5 260 -5 330 55 C430 140 460 300 400 425 L0 425 Z" fill="#0b7fe0"/>
  <g role="img" aria-label="Photo of an aircraft mechanic in a safety vest inspecting landing gear">
    <path d="M0 28 C110 0 250 0 318 58 C412 140 440 300 385 425 L0 425 Z" fill="#8d98a6"/>
  </g>
  <circle cx="420" cy="100" r="60" fill="#e9ebf1"/>
</svg>
<div class="abs about-text">
  <span class="eyebrow">Who we are</span>
  <h2>Safety Excellence<br>Through Expertise</h2>
  <h3>Enhancing Safety, Elevating Standards</h3>
  <p>Lorem ipsum dolor sit amet, consectetur adipiscing elit, sed do eiusmod temp or incididunt ut labore et dolore magna aliqua. Ut enim ad minim veniam, quis laboris nisi ut aliquip ex ea commodo consequat.</p>
  <p style="margin-top:12px">Lorem ipsum dolor sit amet, consectetur adipiscing elit, sed do eiusmod temp or incididunt ut labore et dolore magna aliqua.</p>
  <div class="btn-solid btn-contact">Contact us
    <svg width="16" height="12" viewBox="0 0 16 12"><path d="M1 6h13M9 1l5 5-5 5" fill="none" stroke="#fff" stroke-width="1.6"/></svg>
  </div>
</div>

<section class="abs services">
  <div class="abs center-head" style="top:88px">
    <span class="eyebrow">Our services</span>
    <h2>Services We <span class="accent">Provide</span></h2>
  </div>
</section>
<div class="abs service-card" style="left:118px;top:1654px">
  <div class="service-photo" role="img" aria-label="Photo of two workers in hard hats reviewing a tablet in a warehouse" style="background:linear-gradient(135deg,#8a6a4a,#c9a070 55%,#5a4a3a)"></div>
  <div class="service-body"><h4>Risk Assessments</h4><p>Lorem ipsum dolor sit amet, co nsectetur adipiscing elit, s</p></div>
  <div class="service-icon"><svg width="30" height="30" viewBox="0 0 30 30" fill="none" stroke="#fff" stroke-width="1.6"><circle cx="14" cy="9" r="5"/><path d="M4 26c1-7 5-10 10-10M12 26h14M17 22l6-6 3 3-6 6"/></svg></div>
</div>
<div class="abs service-card" style="left:447px;top:1654px">
  <div class="service-photo" role="img" aria-label="Photo of a team in hard hats discussing around a cardboard box" style="background:linear-gradient(135deg,#6d7680,#b7a58a 55%,#3e4650)"></div>
  <div class="service-body"><h4>Safety Audits</h4><p>Lorem ipsum dolor sit amet, co nsectetur adipiscing elit, s</p></div>
  <div class="service-icon"><svg width="30" height="30" viewBox="0 0 30 30" fill="none" stroke="#fff" stroke-width="1.6"><circle cx="14" cy="9" r="5"/><path d="M4 26c1-7 5-10 10-10M12 26h14M17 22l6-6 3 3-6 6"/></svg></div>
</div>
<div class="abs service-card" style="left:774px;top:1654px">
  <div class="service-photo" role="img" aria-label="Photo of two workers in orange vests reviewing a clipboard in a factory" style="background:linear-gradient(135deg,#3c4756,#7d8a98 55%,#c0662d)"></div>
  <div class="service-body"><h4>Incident Investigation</h4><p>Lorem ipsum dolor sit amet, co nsectetur adipiscing elit, s</p></div>
  <div class="service-icon"><svg width="30" height="30" viewBox="0 0 30 30" fill="none" stroke="#fff" stroke-width="1.6"><circle cx="14" cy="9" r="5"/><path d="M4 26c1-7 5-10 10-10M12 26h14M17 22l6-6 3 3-6 6"/></svg></div>
</div>

<section class="abs why">
  <div role="img" aria-label="Photo of a site engineer in a hi-vis vest reviewing plans at a desk" style="position:absolute;left:0;top:0;width:760px;height:575px;background:linear-gradient(90deg,#c5ccd4 0%,#9aa5b2 45%,rgba(40,60,120,.9) 80%,rgba(12,37,103,0) 100%)"></div>
</section>
<div class="abs why-text">
  <span class="eyebrow">Why choose us</span>
  <h2>Your Partner in <span class="accent">Safety</span><br>and Compliance</h2>
</div>
<div class="abs why-item" style="top:2285px">
  <svg width="40" height="40" viewBox="0 0 30 30" fill="none" stroke="#fff" stroke-width="1.4"><circle cx="14" cy="9" r="5"/><path d="M4 26c1-7 5-10 10-10M12 26h14M17 22l6-6 3 3-6 6"/></svg>
  <div><h4>CLIENT-CENTRIC</h4><p>Lorem ipsum dolor sit amet, consectetur adipiscing elit, sed do eiusmod tempor incidid</p></div>
</div>
<div class="abs why-item" style="top:2398px">
  <svg width="40" height="40" viewBox="0 0 30 30" fill="none" stroke="#fff" stroke-width="1.4"><path d="M15 3l3 4 5 0 1 5 4 3-3 4 1 5-5 1-3 4-3-4-5-1 1-5-3-4 4-3 1-5 5 0z"/></svg>
  <div><h4>PROFESSIONALISM</h4><p>Lorem ipsum dolor sit amet, consectetur adipiscing elit, sed do eiusmod tempor incidid</p></div>
</div>
<div class="abs why-item" style="top:2510px">
  <svg width="40" height="40" viewBox="0 0 30 30" fill="none" stroke="#fff" stroke-width="1.4"><path d="M5 23a11 11 0 1 1 20 0"/><path d="M15 18l5-7"/><circle cx="15" cy="18" r="2"/></svg>
  <div><h4>EXPERIENCED EXPERTS</h4><p>Lorem ipsum dolor sit amet, consectetur adipiscing elit, sed do eiusmod tempor incidid</p></div>
</div>

<section class="abs testimonials">
  <div class="abs center-head" style="top:92px">
    <span class="eyebrow">Testimonials</span>
    <h2>What Clients are <span class="accent">Saying</span></h2>
  </div>
</section>
<div class="abs quote-card" style="left:118px;top:2897px">Lorem ipsum dolor sit amet, consectetur adipiscing elit, sed d o eiusmod tempor incididunt ut lab ore et dolore magna aliqua. Ut enim ad min</div>
<div class="abs quote-tail" style="left:118px;top:3071px"></div>
<div class="abs quote-card active" style="left:446px;top:2897px">Lorem ipsum dolor sit amet, consectetur adipiscing elit, sed d o eiusmod tempor incididunt ut lab ore et dolore magna aliqua. Ut enim ad min</div>
<div class="abs quote-tail" style="left:446px;top:3071px"></div>
<div class="abs quote-card" style="left:776px;top:2897px">Lorem ipsum dolor sit amet, consectetur adipiscing elit, sed d o eiusmod tempor incididunt ut lab ore et dolore magna aliqua. Ut enim ad min</div>
<div class="abs quote-tail" style="left:776px;top:3071px"></div>
<div class="abs author" style="left:136px;top:3096px"><span class="avatar" role="img" aria-label="Client portrait"></span><div><strong>Lena Hart</strong><span>Engineer</span></div></div>
<div class="abs author" style="left:464px;top:3096px"><span class="avatar" role="img" aria-label="Client portrait"></span><div><strong>Lena Hart</strong><span>Engineer</span></div></div>
<div class="abs author" style="left:794px;top:3096px"><span class="avatar" role="img" aria-label="Client portrait"></span><div><strong>Lena Hart</strong><span>Engineer</span></div></div>
<svg class="abs" style="left:569px;top:3195px" width="62" height="12" viewBox="0 0 62 12"><rect x="0" y="1" width="22" height="9" rx="4.5" fill="#0b7fe0"/><circle cx="32" cy="5.5" r="4.5" fill="#0b7fe0"/><circle cx="44" cy="5.5" r="4.5" fill="#0b7fe0"/><circle cx="56" cy="5.5" r="4.5" fill="#0b7fe0"/></svg>

<svg class="abs footer-bg" width="1200" height="638" viewBox="0 0 1200 638">
  <path d="M0 0 C60 120 250 250 730 270 L1200 250 L1200 638 L0 638 Z" fill="#0b7fe0"/>
  <path d="M0 60 C80 170 300 275 730 280 C900 282 1060 270 1200 250 L1200 638 L0 638 Z" fill="#0b1233"/>
  <path d="M0 75 C80 180 300 285 730 275 C520 300 200 260 0 150 Z" fill="#fff"/>
</svg>

<h2 class="abs contact-title">Get In <span class="accent">Touch</span></h2>
<div class="abs contact-box">
  <div class="address-panel">
    <h3>Address</h3>
    <div class="addr-row" style="margin-top:28px"><svg width="22" height="22" viewBox="0 0 22 22" fill="none" stroke="#0b7fe0" stroke-width="1.4"><circle cx="11" cy="7" r="4"/><path d="M3 20c1-6 4-8 8-8s7 2 8 8z"/></svg><div>Company Name<br>Suite 18 Elm Ave<br>City, Country</div></div>
    <div class="addr-row"><svg width="22" height="22" viewBox="0 0 22 22" fill="none" stroke="#0b7fe0" stroke-width="1.4"><path d="M5 3l4 1 1 4-2 2a12 12 0 0 0 5 5l2-2 4 1 1 4c-8 1-17-7-15-15z"/></svg><b style="font-size:13px">720-555-0148 Or 720-555-0172</b></div>
    <div class="addr-row"><svg width="22" height="22" viewBox="0 0 22 22" fill="none" stroke="#0b7fe0" stroke-width="1.4"><rect x="3" y="3" width="16" height="16" rx="2"/><circle cx="11" cy="9" r="3"/><path d="M6 17c1-3 3-4 5-4s4 1 5 4"/></svg><span>contact@corvane-mail.com</span></div>
  </div>
  <div class="field" style="left:325px;top:42px;width:266px">Name:</div>
  <div class="field" style="left:625px;top:42px;width:266px"></div>
  <div class="field" style="left:325px;top:88px;width:266px">Phone:</div>
  <div class="field" style="left:625px;top:88px;width:266px"></div>
  <div class="field" style="left:325px;top:131px;width:563px;height:62px">Details:</div>
  <div class="btn-enquiry">QUICK ENQUIRY <svg width="14" height="10" viewBox="0 0 14 10"><path d="M1 5h11M8 1l4 4-4 4" fill="none" stroke="#fff" stroke-width="1.4"/></svg></div>
</div>

<div class="abs footer-block" style="left:175px;top:4058px;width:272px;padding-left:48px;font-size:12px;line-height:16px">
  <svg width="14" height="18" viewBox="0 0 14 18"><path d="M7 0a7 7 0 0 1 7 7c0 5-7 11-7 11S0 12 0 7a7 7 0 0 1 7-7z" fill="#0b7fe0"/><circle cx="7" cy="7" r="2.5" fill="#0b1233"/></svg>
  <div>42 HARBOR LANE<br>COUNTRY</div>
</div>
<div class="abs brand" style="left:480px;top:4046px">
  <span class="brand-dot" style="width:40px;height:40px"></span><span class="brand-name" style="color:#fff;font-size:44px">Corvane</span>
</div>
<div class="abs footer-block" style="left:760px;top:4058px;width:272px;padding-left:48px;font-size:21px">
  <svg width="14" height="18" viewBox="0 0 14 18"><path d="M7 0a7 7 0 0 1 7 7c0 5-7 11-7 11S0 12 0 7a7 7 0 0 1 7-7z" fill="#0b7fe0"/><circle cx="7" cy="7" r="2.5" fill="#0b1233"/></svg>
  <span>415 555 0192</span>
</div>
<div class="abs" style="left:0;top:4128px;width:1200px;text-align:center;font-size:12px;color:#2d8df0">contact@corvane-mail.com</div>
<div class="abs social" style="left:0;top:4160px;width:1200px"><span></span><span></span><span></span><span></span><span></span></div>
<nav class="abs footer-nav"><a>HOME</a><a>SERVICES</a><a>ABOUT US</a><a>PROJECTS</a><a>TESTIMONIALS</a><a>FAQ</a><a>CONTACT US</a></nav>

</body>
</html>
```